Poster design for a vet clinic

Running a campaign called 'Tail teller', which is where people get a $30 voucher for themselves and their friend if they refer somebody to our vet clinic.

Text something like:
We love Tail Tellers!
Refer a fur friend to our friendly team and both your fur child and their fur child will receive a $30 voucher to use in clinic! *
* Limited to one pet per fur parent and the referred fur parent must be new to our clinic. Unlimited vouchers for number of referrals!

I want it to be cute but professional. You can see the design styles at mossbury-vet.com.au/kelvale and see the logo there too.
I am thinking of having a dog whispering to a cat or something like that as the main image.
I would like both the photoshop file and the pdf please. Would be for an A2 poster.

```html
<!DOCTYPE html>
<html lang="en">
<head>
<meta charset="utf-8">
<title>We Love Tail Tellers! – Mossbury Vet Kelvale</title>
<link href="https://fonts.googleapis.com/css2?family=Archivo+Black&family=Barlow+Semi+Condensed:wght@700&display=swap" rel="stylesheet">
<style>
  :root{
    --backdrop:#262628;
    --sky-deep:#22409a;
    --sky-mid:#3559b0;
    --sky-light:#6f8fd0;
    --fence-brown:#653f36;
    --grass:#bfe06a;
    --grass-dark:#9cca4a;
    --orange:#f28c1c;
    --white:#ffffff;
    --footer-blue:#4f74bf;
    --divider:#e6e6e6;
  }
  *{margin:0;padding:0;box-sizing:border-box}
  html,body{width:894px;height:1200px;overflow:hidden;background:var(--backdrop)}
  .poster{
    position:absolute;left:86px;top:90px;width:722px;height:1020px;
    overflow:hidden;background:var(--sky-mid);
    font-family:"Barlow Semi Condensed",Arial,sans-serif;font-weight:700;color:var(--white);
  }
  .sky-top{
    position:absolute;left:0;top:0;width:722px;height:282px;
    background:linear-gradient(160deg,var(--sky-light) 0%,var(--sky-mid) 35%,var(--sky-deep) 100%);
  }
  .rail{position:absolute;left:0;top:282px;width:722px;height:24px;background:var(--fence-brown)}
  .sky-main{
    position:absolute;left:0;top:306px;width:722px;height:400px;
    background:linear-gradient(200deg,var(--sky-light) 0%,var(--sky-mid) 40%,var(--sky-deep) 100%);
  }
  .brand{
    position:absolute;left:40px;top:126px;width:270px;
    display:flex;align-items:center;gap:12px;
    font-family:"Archivo Black",Arial,sans-serif;font-weight:400;font-size:30px;line-height:1.05;color:var(--white);
  }
  .brand-dot{width:22px;height:22px;border-radius:50%;background:var(--orange);flex:none}
  .headline{
    position:absolute;right:42px;top:30px;text-align:right;
    font-family:"Archivo Black",Arial,sans-serif;font-weight:400;color:var(--white);
    text-shadow:3px 3px 0 var(--fence-brown);text-transform:uppercase;
  }
  .headline span{display:block}
  .headline .line-1{font-size:64px;line-height:70px}
  .headline .line-2{font-size:116px;line-height:104px}
  .headline .line-3{font-size:60px;line-height:70px}
  .offer{
    position:absolute;left:40px;width:642px;text-align:center;
    font-size:20px;line-height:26px;text-transform:uppercase;
  }
  .offer-main{top:344px}
  .offer-terms{top:458px}
  .scene-grass{
    position:absolute;left:0;top:610px;width:722px;height:110px;
    background:linear-gradient(180deg,var(--grass-dark),var(--grass));
  }
  .art-kennel{
    position:absolute;left:18px;top:518px;width:180px;height:150px;
    background:linear-gradient(180deg,var(--white),#f7d9b4);border-radius:6px;
  }
  .art-cat{
    position:absolute;left:556px;top:494px;width:134px;height:148px;
    background:linear-gradient(180deg,#f9c48a,var(--white));border-radius:6px;
  }
  .art-fence{
    position:absolute;left:0;top:690px;width:722px;height:132px;
    background:linear-gradient(180deg,var(--white) 0%,#f2efec 80%,var(--fence-brown) 100%);
  }
  .divider{position:absolute;left:0;top:822px;width:722px;height:14px;background:var(--divider)}
  .footer{position:absolute;left:0;top:836px;width:722px;height:184px;background:var(--white)}
  .footer-panel{position:absolute;left:0;top:0}
  .address{
    position:absolute;left:54px;top:32px;font-size:24px;line-height:30px;text-transform:uppercase;
  }
  .contact{
    position:absolute;left:54px;display:flex;align-items:center;gap:14px;
    font-size:25px;line-height:30px;text-transform:uppercase;
  }
  .contact-phone{top:100px}
  .contact-email{top:132px}
  .contact svg{width:26px;height:26px;flex:none}
  .footer-brand{
    position:absolute;left:460px;top:62px;width:230px;
    display:flex;align-items:center;gap:12px;
    font-family:"Archivo Black",Arial,sans-serif;font-weight:400;font-size:28px;line-height:1.05;color:var(--fence-brown);
  }
</style>
</head>
<body>
<main class="poster">
  <div class="sky-top"></div>
  <div class="brand"><span class="brand-dot"></span><span>Mossbury Vet Kelvale</span></div>
  <h1 class="headline">
    <span class="line-1">We Love</span>
    <span class="line-2">Tail</span>
    <span class="line-3">Tellers!</span>
  </h1>
  <div class="rail"></div>
  <div class="sky-main"></div>

  <div class="scene-grass" role="img" aria-label="Green lawn grass"></div>
  <div class="art-kennel" role="img" aria-label="Cartoon dog peeking out of an orange and white kennel"></div>
  <div class="art-cat" role="img" aria-label="Cartoon cat sitting in an orange-trimmed box"></div>

  <p class="offer offer-main">Refer a fur friend to our friendly team and both your<br>fur child and their fur child will receive a $30<br>voucher to use in clinic!</p>
  <p class="offer offer-terms">*Limited to one pet per fur parent and the referred<br>fur parent must be new to our clinic.<br>Unlimited vouchers for<br>number of referrals!</p>

  <div class="art-fence" role="img" aria-label="White picket fence"></div>
  <div class="divider"></div>

  <footer class="footer">
    <svg class="footer-panel" width="722" height="184" viewBox="0 0 722 184" aria-hidden="true">
      <polygon points="0,0 434,0 326,184 0,184" fill="var(--footer-blue)"/>
    </svg>
    <p class="address">27 Larkspur Avenue<br>Kelvale, NSW, 2190</p>
    <p class="contact contact-phone">
      <svg viewBox="0 0 26 26" aria-hidden="true"><circle cx="13" cy="13" r="13" fill="#fff"/><path d="M9 7c1 0 2 2.5 2 3s-1 1-1 1.6c0 1 3 4 4 4 .6 0 1-1 1.6-1s3 1 3 2-1.2 2.4-2.6 2.4C11 19 7 15 7 9.4 7 8 8 7 9 7z" fill="var(--footer-blue)"/></svg>
      <span>02 5550 1427</span>
    </p>
    <p class="contact contact-email">
      <svg viewBox="0 0 26 26" aria-hidden="true"><circle cx="13" cy="13" r="13" fill="#fff"/><rect x="6.5" y="8.5" width="13" height="9" fill="none" stroke="var(--footer-blue)" stroke-width="1.6"/><path d="M6.5 8.5 13 14l6.5-5.5" fill="none" stroke="var(--footer-blue)" stroke-width="1.6"/></svg>
      <span>Email us</span>
    </p>
    <div class="footer-brand"><span class="brand-dot"></span><span>Mossbury Vet Kelvale</span></div>
  </footer>
</main>
</body>
</html>
```